依頼概要
■依頼の目的/概要
通販限定の高級冷凍カレーのラベルデザイン。
(既存ラベルのリニューアル)

■ラベルサイズ
縦7センチ×横9センチ
(縦10センチ×横14センチ程のカレールーに貼るので、ラベルの周囲に
こげ茶色のカレールーが見えます。サイズイメージの添付ファイルご参照
ください。)

■ラベルに表記したい事項
①商品名:ほのぼのカレー 水辺ルビー
(縦書きでも横書きでも結構です。また、「ほのぼのカレー」は
小さめの字にして添える感じでも結構です。 )
②弊店ロゴ
(添付ファイル3枚目のロゴを使って下さい。色は自由に変えて下さい。)

■載せても載せなくても良い事項(デザイン優先)
①Mizube Ruby 又はMIZUBE RUBY
②贅沢仕込みの最高級
③通販限定

■依頼詳細
・商品名の由来ですが、日本の国民食と言われるカレーを、世界でも
ゴールドメダルを獲得できるような料理として東京から発信したい、という
気持ちで付けました。

また、実店舗では「森の藍色」という名前のカレーを提供しておりますが、
通販商品に関しては、さらに素材や調理方法にこだわって贅沢にお作りした
という意味もあります。

・高単価のカレー(3食入り5400円)ですので、和風洋風問わず、美しく
高級感があり、印象に残るデザインを希望します。

■その他
・既にリピーター様も多くいらっしゃる弊店の看板商品です。
今回デザインして頂いたラベルは、長く大切に使わせて頂きたいと
思っております。

その他何かご不明な点がございましたら、お気軽にご質問下さい。
どうぞよろしくお願いいたします。
お世話になっております。

依頼した際に、参考資料として商品写真を添付致しましたが、ラベルに必ず入れて頂きたい事項は商品名とロゴの2つだけです。それ以外はデザイン優先で大丈夫です。

また、ラベルの縦横は逆にしないようにお願いします。
縦7センチ×横9センチです。
(縦9センチ×横7センチは不可です。)

個性的で洗練されたデザインを希望しています。

引き続きどうぞ宜しくお願い申し上げます。
お世話になっております。
また、既にご提案を下さっているデザイナー様には心より感謝申し上げます。

この度の募集期間ですが、締め切りを5月9日までに延長させて頂くことになりました。

また、デザインについての補足ですが、店頭に並ぶわけではありませんので(通販限定商品のため)ビーフカレーであることや辛口であること等、どのようなカレーかをラベルで伝える必要はありません。

通販サイトで画像をご覧になった方が、パッと目を引くような個性的で洗練された「イメージ」が伝わるラベルのデザインを希望します。

引き続きどうぞ宜しくお願い申し上げます。
■ 選んだ理由

インパクトやサイト内で目にした時の印象だけではなく、お客様が実際に冷凍庫から商品を取り出して調理する時も、華やかな気持ちなって頂けるのでは、と思いました。

■ 提案者全員のお礼・コメント

連休中にもかかわらず、たくさんのデザイナー様にご提案頂き、心より感謝申し上げます。
店舗運営をしておりますと、メニュー、フライヤー、ショップカード、パッケージ等々の作成に直面する事が多く、皆様のお力をお借りできる場が有り、大変有難く思っております。
私共の思いが、より明確に伝わるような依頼の仕方を心がけていきますので、今後ともどうぞ宜しくお願い申し上げます。

```html
<!DOCTYPE html>
<html lang="ja">
<head>
<meta charset="utf-8">
<title>ほのぼのカレー 水辺ルビー ラベル</title>
<link rel="stylesheet" href="https://fonts.googleapis.com/css2?family=Cinzel:wght@400&family=Noto+Serif+JP:wght@500;700&display=swap">
<style>
  :root {
    --paper: #ffffff;
    --card-line: #c9c9c9;
    --ink: #111111;
    --gold: #b39a4c;
    --gold-soft: #d8c793;
  }
  * { box-sizing: border-box; margin: 0; padding: 0; }
  html, body { width: 849px; height: 1200px; overflow: hidden; background: var(--paper); }
  .sheet { position: relative; width: 849px; height: 1200px; }
  .card {
    position: absolute; left: 62px; width: 738px; height: 461px;
    border: 1.5px solid var(--card-line); background: var(--paper);
  }
  .card--first { top: 62px; }
  .card--second { top: 670px; }
  .label {
    position: absolute; left: 33px; top: 44px; width: 670px; height: 382px;
    border: 7px solid var(--ink); background: var(--paper);
  }
  .label__frame {
    position: absolute; inset: 10px; border: 1.5px solid var(--gold);
  }
  .label__emblem {
    position: absolute; left: 50%; top: 46px; width: 120px; height: 118px;
    transform: translateX(-50%);
    background: radial-gradient(circle at 50% 45%, #3a3a3a, #111 70%);
    border-radius: 50% 50% 44% 44%;
  }
  .label__brand {
    position: absolute; left: 0; right: 0; top: 178px; text-align: center;
    font-family: "Cinzel", serif; font-weight: 400; font-size: 34px;
    letter-spacing: 1px; color: var(--gold);
  }
  .label__band {
    position: absolute; left: 10px; right: 10px; top: 228px; height: 44px;
    background: var(--ink); color: var(--paper);
    display: flex; align-items: center; justify-content: center;
    font-family: "Noto Serif JP", serif; font-weight: 500; font-size: 16px; letter-spacing: 2px;
  }
  .label__band-gap { display: inline-block; width: 14px; }
  .label__plate {
    position: absolute; left: 18px; right: 18px; top: 282px; height: 62px;
    border: 1.5px solid var(--gold);
  }
  .badge {
    position: absolute; left: 610px; top: 19px; width: 86px; height: 96px;
  }
  .badge__text {
    position: absolute; inset: 0; display: flex; flex-direction: column;
    align-items: center; justify-content: center; gap: 6px;
    font-family: "Noto Serif JP", serif; color: var(--paper);
  }
  .badge__main { font-size: 12px; font-weight: 700; letter-spacing: 1px; }
  .badge__sub { font-size: 7px; font-weight: 500; line-height: 1.3; text-align: center; }
</style>
</head>
<body>
<main class="sheet">
  <section class="card card--first">
    <div class="label">
      <div class="label__frame"></div>
      <div class="label__emblem" role="img" aria-label="Shop crest emblem"></div>
      <div class="label__brand">MAISON DE RIVE</div>
      <div class="label__band">ほのぼのカレー<span class="label__band-gap"></span>水辺ルビー</div>
      <div class="label__plate"></div>
    </div>
    <div class="badge">
      <svg width="86" height="96" viewBox="0 0 86 96">
        <polygon points="25,2 61,2 84,26 84,70 61,94 25,94 2,70 2,26" fill="var(--gold)"/>
      </svg>
      <div class="badge__text">
        <span class="badge__main">通販限定</span>
        <span class="badge__sub">贅沢仕込みの<br>最高級</span>
      </div>
    </div>
  </section>

  <section class="card card--second">
    <div class="label">
      <div class="label__frame"></div>
      <div class="label__emblem" role="img" aria-label="Shop crest emblem"></div>
      <div class="label__brand">MAISON DE RIVE</div>
      <div class="label__band">ほのぼのカレー<span class="label__band-gap"></span>水辺ルビー</div>
      <div class="label__plate"></div>
    </div>
  </section>
</main>
</body>
</html>
```